Home page redesign for an international job board

Need a modern design based on current structure of the page. I am happy with the current structure and layout/architecture, not entirely happy with how it looks. While I still want to keep most of the elements in place ( especially the search box) I would like to get another look and feel - more appealing to any audience related to online job search

Home page is: www.drumvaliant.ro

Target Market(s)

job seeekers and employers

Industry/Entity Type

Architecture

Number of Pages Required

1 page

Font styles to use
Sans Serif

Colors
33a6d7

Requirements
Must have
• Stay with the same structure: Seach box, latest jobs, articles
Nice to have
• Key element: search for jobs - this needs to be very clear

```html
<!DOCTYPE html>
<html lang="en">
<head>
<meta charset="utf-8">
<title>DrumValiant – Job Board Home</title>
<link href="https://fonts.googleapis.com/css2?family=Roboto:wght@400;500;700&family=Roboto+Condensed:wght@400;700&display=swap" rel="stylesheet">
<style>
:root{
  --brand:#33a6d7;
  --brand-dark:#2b95c4;
  --navy:#123e5c;
  --ink:#333;
  --text:#555;
  --muted:#888;
  --line:#e3e3e3;
  --accent:#d9382d;
  --star:#f0a21c;
  --dark-band:#1e2326;
  --bottom:#2b2b2b;
  --white:#fff;
}
*{box-sizing:border-box;margin:0;padding:0}
html,body{width:1200px;height:2429px;overflow:hidden;background:var(--white)}
body{position:relative;font-family:"Roboto",Arial,sans-serif;color:var(--text)}
.abs{position:absolute}

/* top strip */
.top-strip{position:absolute;left:0;top:0;width:1200px;height:4px;background:#333}
.top-strip span{position:absolute;left:401px;width:392px;height:4px;background:var(--accent)}
.top-bar{position:absolute;left:0;top:4px;width:1200px;height:35px;border-bottom:1px solid var(--line)}
.top-links{position:absolute;right:99px;top:10px;font-size:12px;color:#444;letter-spacing:.3px}
.top-links i{font-style:normal;margin:0 8px;color:#999}

/* header */
.site-header{position:absolute;left:0;top:39px;width:1200px;height:81px}
.brand{position:absolute;left:97px;top:22px;display:flex;align-items:center;gap:10px;font-size:27px;font-weight:500;color:var(--ink)}
.brand-dot{width:34px;height:34px;border-radius:50%;background:var(--accent)}
.main-nav{position:absolute;top:33px;left:0;font-size:13px;color:#333;letter-spacing:.3px}
.main-nav a{position:absolute;white-space:nowrap;color:inherit;text-decoration:none}
.btn-post{position:absolute;left:921px;top:24px;width:180px;height:36px;background:var(--brand);color:#fff;border-radius:3px;font-size:13px;line-height:36px;text-align:center;letter-spacing:.3px}

/* hero */
.hero{position:absolute;left:0;top:120px;width:1200px;height:539px;background:linear-gradient(100deg,#3a4a52 0%,#7d8f99 30%,#c7d3d9 55%,#8ea2ae 75%,#4d5e68 100%)}
.hero-title{position:absolute;left:115px;top:208px;font-family:"Roboto Condensed",Arial,sans-serif;font-weight:700;font-size:46px;color:#fff;letter-spacing:.5px}
.hero-sub{position:absolute;left:117px;top:268px;font-size:14px;line-height:21px;color:#fff;font-weight:500}
.hero-arrow{position:absolute;top:254px;width:30px;height:30px;border-radius:50%;background:rgba(60,60,60,.6)}

/* search panel */
.search-panel{position:absolute;left:97px;top:576px;width:1006px;height:217px;background:var(--brand);border-radius:3px;box-shadow:0 18px 22px -12px rgba(0,0,0,.35)}
.search-head{height:54px;border-bottom:1px solid rgba(255,255,255,.35);padding-left:41px;font-family:"Roboto Condensed",Arial,sans-serif;font-size:20px;line-height:54px;color:#fff}
.search-label{position:absolute;top:76px;font-size:13px;color:#fff;font-weight:500}
.field{position:absolute;width:301px;height:37px;background:#fff;border-radius:2px;font-size:11px;color:#888;line-height:37px;padding-left:16px}
.field svg{position:absolute;right:40px;top:15px}
.btn-search{position:absolute;left:670px;top:151px;width:144px;height:38px;background:var(--navy);color:#fff;font-size:13px;line-height:38px;text-align:center;border-radius:2px}
.adv-link{position:absolute;left:834px;top:163px;font-size:13px;color:#fff}

/* intro */
.intro-title{position:absolute;left:0;top:842px;width:1200px;text-align:center;font-family:"Roboto Condensed",Arial,sans-serif;font-size:30px;color:#2a2a2a}
.intro-text{position:absolute;left:170px;top:889px;width:860px;text-align:center;font-size:12px;line-height:21px;color:#666}
.feature{position:absolute;top:960px;width:329px;height:112px;border:1px solid var(--line)}
.feature-icon{position:absolute;left:27px;top:20px;width:71px;height:71px;border-radius:50%;display:flex;align-items:center;justify-content:center}
.feature-title{position:absolute;left:133px;top:28px;font-size:15px;color:#333;letter-spacing:.3px}
.feature-text{position:absolute;left:133px;top:54px;width:185px;font-size:12px;line-height:20px;color:#666}
.feature-corner{position:absolute;right:0;bottom:0;width:0;height:0;border-left:16px solid transparent;border-bottom:16px solid #ddd}

/* apps band */
.apps-band{position:absolute;left:0;top:1127px;width:1200px;height:424px;background:linear-gradient(90deg,#2a3034 0%,#1a1f22 45%,#262c30 100%)}
.app{position:absolute;top:56px;width:360px;text-align:center;color:#fff}
.app-thumb{width:155px;height:155px;border-radius:50%;margin:0 auto;border:4px solid #ddd;background:radial-gradient(circle at 50% 45%,#e9eef2 0%,#a7b3bb 60%,#6f7b83 100%)}
.app-title{margin-top:24px;font-size:18px}
.app-text{margin-top:12px;font-size:12px;line-height:19px;color:#e6e6e6}
.app-btn{display:inline-block;margin-top:18px;width:143px;height:36px;border:1px solid #ddd;font-size:12px;line-height:34px;letter-spacing:.3px}

/* latest jobs & testimonials */
.col-head{position:absolute;top:1598px;font-size:23px;color:#333}
.col-rule{position:absolute;top:1638px;height:1px;background:var(--line)}
.job-thumb{position:absolute;left:99px;width:171px;height:104px;background:linear-gradient(135deg,#cfdbe5 0%,#8aa1b3 50%,#3f5468 100%)}
.job-title{position:absolute;left:293px;font-size:15px;color:#333}
.job-date{position:absolute;left:293px;font-size:13px;color:var(--accent);font-weight:500}
.job-text{position:absolute;left:293px;width:272px;font-size:12px;line-height:19px;color:#555}
.avatar{position:absolute;left:668px;width:104px;height:104px;border-radius:50%;border:1px solid var(--line);background:radial-gradient(circle at 50% 40%,#e8ecef 0%,#b9c3ca 70%,#8d99a2 100%)}
.quote-mark{position:absolute;left:798px;font-size:24px;color:#666;font-family:Georgia,serif}
.quote{position:absolute;left:812px;width:292px;font-size:12px;line-height:21px;font-style:italic;color:#555}
.reviewer{position:absolute;left:800px;font-size:12px;color:var(--accent);font-weight:500}
.stars{position:absolute;left:876px;display:flex;gap:2px}

/* callout */
.callout{position:absolute;left:97px;top:1956px;width:1006px;height:157px;border:2px solid #b9dff0;padding:30px 30px 0}
.callout h2{font-size:21px;font-weight:500;color:var(--brand-dark);letter-spacing:.2px}
.callout p{margin-top:12px;font-size:12px;line-height:21px;color:#666}

/* footer */
.site-footer{position:absolute;left:0;top:2153px;width:1200px;height:219px;background:var(--brand);color:#fff}
.foot-head{position:absolute;top:44px;font-size:15px;font-weight:500;letter-spacing:.2px}
.foot-list{position:absolute;top:76px;list-style:none;font-size:12px;line-height:24.4px}
.foot-list li::before{content:"›";margin-right:12px}
.foot-note{position:absolute;left:584px;top:78px;width:300px;font-size:11px;line-height:18px}
.news-input{position:absolute;left:584px;top:131px;width:201px;height:41px;background:#fff;color:#555;font-size:11px;line-height:41px;padding-left:14px}
.news-btn{position:absolute;left:785px;top:131px;width:81px;height:41px;background:var(--navy);font-size:12px;line-height:41px;text-align:center}
.contact-line{position:absolute;left:931px;font-size:13px}
.bottom-bar{position:absolute;left:0;top:2372px;width:1200px;height:57px;background:var(--bottom);color:#ddd;font-size:12px;text-align:center;line-height:57px}
</style>
</head>
<body>

<div class="top-strip"><span></span></div>
<div class="top-bar"><div class="top-links">REGISTER<i>|</i>LOG IN</div></div>

<header class="site-header">
  <div class="brand"><span class="brand-dot"></span>DrumValiant</div>
  <nav class="main-nav">
    <a style="left:406px">SEARCH JOB</a>
    <a style="left:529px">MY ACCOUNT</a>
    <a style="left:656px">CAREER COUNSELING</a>
    <a style="left:834px">CONTACT</a>
  </nav>
  <div class="btn-post">EMPLOYER &amp; POST JOB</div>
</header>

<section class="hero" role="img" aria-label="Photo of three young colleagues working together at a laptop">
  <div class="hero-title">DRUM VALIANT</div>
  <div class="hero-sub">Lorem ipsum dolor sit amet, consectetur adipiscing elit,<br>sed do eiusmod tempor incididunt ut labore et</div>
  <div class="hero-arrow" style="left:45px"><svg width="30" height="30"><path d="M17 9l-6 6 6 6" fill="none" stroke="#fff" stroke-width="2"/></svg></div>
  <div class="hero-arrow" style="left:1126px"><svg width="30" height="30"><path d="M13 9l6 6-6 6" fill="none" stroke="#fff" stroke-width="2"/></svg></div>
</section>

<section class="search-panel">
  <div class="search-head">SEARCH JOB CREATES ACCOUNT</div>
  <div class="search-label" style="left:34px">Search Job</div>
  <div class="search-label" style="left:351px">Region</div>
  <div class="search-label" style="left:670px">Work Type</div>
  <div class="field" style="left:34px;top:99px">Keywords (IT Engineer, Shop Manager)<svg width="9" height="6"><path d="M1 1l3.5 3.5L8 1" fill="none" stroke="#888"/></svg></div>
  <div class="field" style="left:351px;top:99px">Select<svg width="9" height="6"><path d="M1 1l3.5 3.5L8 1" fill="none" stroke="#888"/></svg></div>
  <div class="field" style="left:670px;top:99px">Any Employment Type<svg width="9" height="6"><path d="M1 1l3.5 3.5L8 1" fill="none" stroke="#888"/></svg></div>
  <div class="field" style="left:34px;top:151px">Select Category<svg width="9" height="6"><path d="M1 1l3.5 3.5L8 1" fill="none" stroke="#888"/></svg></div>
  <div class="field" style="left:351px;top:151px">Classification<svg width="9" height="6"><path d="M1 1l3.5 3.5L8 1" fill="none" stroke="#888"/></svg></div>
  <div class="btn-search">SEARCH JOB</div>
  <div class="adv-link">ADVANCE SEARCH</div>
</section>

<h1 class="intro-title">SEARCH JOB CREATES ACCOUNT APPLY JOB OF MOBILE</h1>
<p class="intro-text">Lorem ipsum dolor sit amet, consectetur adipiscing elit, sed do eiusmod tempor incididunt ut labore et dolore magna aliqua. Ut enim ad minim veniam, quis nostrud exercitation ullamco laboris nisi ut aliquip ex ea commodo consequat. Duis aute irure dolor in reprehenderit in voluptate velit esse</p>

<div class="feature" style="left:97px">
  <div class="feature-icon" style="background:#444">
    <svg width="38" height="30" viewBox="0 0 38 30"><path d="M19 3L2 11l17 8 17-8z" fill="#fff"/><path d="M9 15v7c0 3 5 5 10 5s10-2 10-5v-7l-10 5z" fill="#fff"/><path d="M33 12v10" stroke="#fff" stroke-width="2"/></svg>
  </div>
  <div class="feature-title">POST CV</div>
  <div class="feature-text">Lorem ipsum dolor sit amet, consectetur adipiscing elit, sed</div>
  <div class="feature-corner"></div>
</div>
<div class="feature" style="left:434px">
  <div class="feature-icon" style="background:var(--brand)">
    <svg width="28" height="30" viewBox="0 0 28 30"><circle cx="14" cy="8" r="7" fill="#fff"/><path d="M1 29c0-8 6-12 13-12s13 4 13 12z" fill="#fff"/></svg>
  </div>
  <div class="feature-title">CREATE ALERTS JOBS</div>
  <div class="feature-text">Lorem ipsum dolor sit amet, consectetur adipiscing elit, sed</div>
  <div class="feature-corner"></div>
</div>
<div class="feature" style="left:772px">
  <div class="feature-icon" style="background:var(--brand)">
    <svg width="34" height="30" viewBox="0 0 34 30"><rect x="2" y="2" width="30" height="20" rx="2" fill="none" stroke="#fff" stroke-width="3"/><path d="M12 28h10M17 22v6" stroke="#fff" stroke-width="3"/></svg>
  </div>
  <div class="feature-title">MONITORING APP JOBS</div>
  <div class="feature-text">Lorem ipsum dolor sit amet, consectetur adipiscing elit, sed</div>
  <div class="feature-corner"></div>
</div>

<section class="apps-band" role="img" aria-label="Dark background photo of a businessman looking down at a phone">
  <div class="app" style="left:77px">
    <div class="app-thumb" role="img" aria-label="Job app screens shown on a phone"></div>
    <div class="app-title">Jobs apps for Phones</div>
    <div class="app-text">Lorem ipsum dolor sit amet, conse adipisic ing elit,<br>sed do eiusmod tempor incididunt</div>
    <div class="app-btn">DOWNLOAD NOW</div>
  </div>
  <div class="app" style="left:426px">
    <div class="app-thumb" role="img" aria-label="Job app screens shown on a tablet"></div>
    <div class="app-title">Jobs apps for Tablets</div>
    <div class="app-text">Lorem ipsum dolor sit amet, conse adipisic ing elit,<br>sed do eiusmod tempor incididunt</div>
    <div class="app-btn">DOWNLOAD NOW</div>
  </div>
  <div class="app" style="left:774px">
    <div class="app-thumb" role="img" aria-label="Hand holding a smartphone with a social job page"></div>
    <div class="app-title">Jobs Requirement Social Networks</div>
    <div class="app-text">Lorem ipsum dolor sit amet, conse adipisic ing elit,<br>sed do eiusmod tempor incididunt</div>
    <div class="app-btn">JOIN NOW</div>
  </div>
</section>

<h2 class="col-head" style="left:97px">LATEST JOBS</h2>
<div class="col-rule" style="left:97px;width:468px"></div>
<h2 class="col-head" style="left:667px">TESTIMONIALS</h2>
<div class="col-rule" style="left:667px;width:434px"></div>

<div class="job-thumb" style="top:1664px" role="img" aria-label="Photo of business people meeting at a table"></div>
<div class="job-title" style="top:1662px">Nemo Enim Ipsam Voluptatem</div>
<div class="job-date" style="top:1692px">JULY 20, 2015</div>
<div class="job-text" style="top:1715px">Lorem ipsum dolor sit amet, consectetur adipiscing elit, sed do eiusmod tempor incididunt ut labore et dolore magna aliqua.</div>

<div class="job-thumb" style="top:1797px" role="img" aria-label="Photo of a team working in an office"></div>
<div class="job-title" style="top:1795px">Nemo Enim Ipsam Voluptatem</div>
<div class="job-date" style="top:1825px">JULY 20, 2015</div>
<div class="job-text" style="top:1848px">Lorem ipsum dolor sit amet, consectetur adipiscing elit, sed do eiusmod tempor incididunt ut labore et dolore magna aliqua.</div>

<div class="avatar" style="top:1667px" role="img" aria-label="Portrait photo of a reviewer in a suit"></div>
<div class="quote-mark" style="top:1668px">“</div>
<div class="quote" style="top:1673px">Lorem ipsum dolor sit amet, consectetur adipiscing elit, sed do eiusmod tempor incididunt ut labore et dolore magna aliqua. Ut enim ad minim veniam, quis nostrud</div>
<div class="reviewer" style="top:1747px">JOHN DOE</div>
<div class="stars" style="top:1748px">
  <svg width="60" height="12" viewBox="0 0 60 12"><g fill="var(--star)"><path id="st" d="M6 0l1.8 3.8 4.2.5-3.1 2.9.8 4.1L6 9.3 2.3 11.3l.8-4.1L0 4.3l4.2-.5z"/><use href="#st" x="12"/><use href="#st" x="24"/></g><g fill="none" stroke="var(--star)" stroke-width=".8"><use href="#st" x="36"/><use href="#st" x="48"/></g></svg>
</div>

<div class="avatar" style="top:1805px" role="img" aria-label="Portrait photo of a second reviewer in a suit"></div>
<div class="quote-mark" style="top:1806px">“</div>
<div class="quote" style="top:1811px">Lorem ipsum dolor sit amet, consectetur adipiscing elit, sed do eiusmod tempor incididunt ut labore et dolore magna aliqua. Ut enim ad minim veniam, quis nostrud</div>
<div class="reviewer" style="top:1885px">JOHN DOE</div>
<div class="stars" style="top:1886px">
  <svg width="60" height="12" viewBox="0 0 60 12"><g fill="var(--star)"><use href="#st"/><use href="#st" x="12"/><use href="#st" x="24"/></g><g fill="none" stroke="var(--star)" stroke-width=".8"><use href="#st" x="36"/><use href="#st" x="48"/></g></svg>
</div>

<section class="callout">
  <h2>NEQUE PORRO QUISQUAM EST QUI DOLOREM IPSUM QUIA DOLOR SIT AMET</h2>
  <p>Lorem Ipsum has been the industry's standard dummy text ever since the 1500s, when an unknown printer took a galley of type and scrambled it to make a type specimen book. It has survived not only five centuries, but also the leap into electronic typesetting, remaining essentially unchanged Lorem Ipsum has been the industry's standard dummy text ever since the 1500s, when an unknown printer took a galley of type and scrambled it to make a type specimen book.</p>
</section>

<footer class="site-footer">
  <h3 class="foot-head" style="left:97px">EMPLOYER TOOLS</h3>
  <ul class="foot-list" style="left:100px">
    <li>Post job ads</li><li>Access Jobseekers</li><li>Resume Search</li><li>Analytics</li><li>Employer Tools</li>
  </ul>
  <h3 class="foot-head" style="left:345px">JOB SEEKER TOOLS</h3>
  <ul class="foot-list" style="left:348px">
    <li>Resume Posting</li><li>Job Alerts</li><li>Video Resume</li><li>Create Profile</li>
  </ul>
  <h3 class="foot-head" style="left:584px">OUR NEWSLETTER</h3>
  <p class="foot-note">Excepteur sint occaecat cupidatat non proident, sunt in culpa qui Excepteur sint occaecat</p>
  <div class="news-input">Enter Name</div>
  <div class="news-btn">SIGN UP</div>
  <h3 class="foot-head" style="left:931px;top:41px">CONTACT US</h3>
  <div class="contact-line" style="top:76px">Drum Valiant</div>
  <div class="contact-line" style="top:96px">4100 LV&nbsp; Valea Lină</div>
  <div class="contact-line" style="top:130px">
    <svg width="16" height="16" viewBox="0 0 16 16" style="vertical-align:-3px;margin-right:14px"><path d="M3 1l3 3-1.5 2c1 2 3 4 5 5L11.5 9.5l3 3-2 2.5C7 14 2 9 1 3z" fill="none" stroke="#fff" stroke-width="1.3"/></svg>+40 555 0123 4567</div>
  <div class="contact-line" style="top:155px">
    <svg width="16" height="12" viewBox="0 0 16 12" style="vertical-align:-1px;margin-right:14px"><rect x=".7" y=".7" width="14.6" height="10.6" fill="none" stroke="#fff" stroke-width="1.3"/><path d="M1 1l7 6 7-6" fill="none" stroke="#fff" stroke-width="1.3"/></svg>info@drumvaliant.ro</div>
</footer>

<div class="bottom-bar">Copyright©2015 Drum Valiant. Terms &nbsp;/&nbsp; Privacy</div>

</body>
</html>
```